Gordon Pellbrook Consulting - Web Design Project

We need a web design for my new edgy consulting business specializing in innovation, technology and strategy.

It is our personal goal to turn each client into raving fans by helping them achieve their own business goals and aspirations through assisting them in raising their own innovation and marketing standards.

We provide our personalised and state-of-the-art services to our clients and boards who represent some of the world greatest innovative thinkers.
Updates

Here is some other information which may help shape your thinking.

I've had direct Involvement in the development of the following iPad, iPhone Applications and websites

FarbeyondOzlands.com (TerraLink platform) by Voyage Bureau
http://farbeyondozlands.example.au

Sail Verve by Bright Voyaging
https://apps.example-store.com/au/app/sail-verve/id100000001

uRedlandTR by Travel Territory Board
https://apps.example-store.com/au/app/uredlandtr/id100000002

Wexmoor Trips
http://www.wexmoortrips.example.au

Trek Mapper by Voyage Bureau
http://apps.example-store.com/au/app/trek-mapper/id100000003

Sunward by Sunward Travel Office
https://apps.example-store.com/au/app/sunward/id100000004

Upper Fernridge Valley Route by Visit Coastlands
https://apps.example-store.com/au/app/upper-fernridge-valley-route/id100000005

Wanderer Path by Travel Territory Board and Southern Plains Travel Council
https://apps.example-store.com/au/app/wanderers-path-grand-journey/id100000006

Gordon Pellbrook Consulting (GPC)
November 2012 – Present (8 months)Brisbane, Sydney, Canberra

Gordon’s consults to Small-to-Medium Enterprises (SME) and Government organisations on business strategy, technology strategy, risk mitigation, disruptive technology and innovation in the workplace.

Gordon’s consultancy mantra is that we cannot divorce economic life from cultural life particularly in an era when social capital may be as important as physical capital in business.

Reason: request from designers, I want to see their best efforts

Target Market(s)

35+

Industry/Entity Type

Business

Requirements
Must have
• Please use some of the personal image(s) contained in the zip files which can be downloaded from here

http://filedrop.example/k9Xq2Lm
http://filedrop.example/p4Rt7Vn
http://filedrop.example/z8Hw3Bc
Nice to have
• Black, Sleek design, maybe minimalist. Nice to have a Pixelle for the design. Nice to have it easily ported to Wordpress or be a modified Wordpress template. HTML 5, responsive design

```html
<!DOCTYPE html>
<html lang="en">
<head>
<meta charset="utf-8">
<title>Gordon Pellbrook Consulting</title>
<link href="https://fonts.googleapis.com/css2?family=Open+Sans:ital,wght@0,400;0,600;0,700;1,400&display=swap" rel="stylesheet">
<style>
:root{
  --teal:#4f8f86;
  --teal-dark:#3f7a72;
  --teal-light:#6aa9a0;
  --ink:#222;
  --text:#555;
  --muted:#888;
  --soft:#f3f4f4;
  --line:#dcdcdc;
  --footer:#2f2f2f;
  --footer-deep:#232323;
  --white:#fff;
}
*{box-sizing:border-box;margin:0;padding:0}
html,body{width:749px;height:1200px;overflow:hidden}
body{font-family:"Open Sans",Arial,sans-serif;color:var(--text);background:var(--white);position:relative}
.abs{position:absolute}
.topbar{left:0;top:0;width:749px;height:19px;background:var(--teal);color:#e8f2f0;font-size:7px;line-height:19px}
.topbar span{position:absolute}
.dot-social{position:absolute;top:3px;width:13px;height:13px;border-radius:50%;background:rgba(255,255,255,.35)}
.header{left:0;top:19px;width:749px;height:62px;background:var(--white);box-shadow:0 1px 3px rgba(0,0,0,.08)}
.brand{left:106px;top:11px}
.brand-name{font-size:20px;font-weight:700;color:var(--ink);line-height:22px}
.brand-name em{font-style:normal;color:var(--teal)}
.brand-tag{font-size:7.5px;color:var(--muted);letter-spacing:.2px}
.nav{left:294px;top:10px;height:40px;display:flex;font-size:9.5px;color:var(--ink)}
.nav a{display:block;padding:0 12.5px;line-height:40px;text-decoration:none;color:inherit}
.nav a.active{color:var(--teal);font-weight:600;border-bottom:2px solid var(--teal);border-left:1px solid #eee;border-right:1px solid #eee}
.hero{left:0;top:81px;width:749px;height:228px;background:linear-gradient(90deg,#eef1f1 0%,#e3eaec 40%,#edf2f3 100%)}
.hero-leaf{left:0;top:34px;width:80px;height:194px;background:linear-gradient(180deg,#c5d9b4,#dfe9d6)}
.portrait{left:108px;top:0;width:236px;height:228px;background:linear-gradient(180deg,#cfd8de 0%,#8aa3b6 55%,#6f8aa0 100%)}
.bubble{width:88px;height:88px;border-radius:50%;background:var(--white);border:5px solid var(--teal);box-shadow:0 0 0 3px #fff,0 2px 6px rgba(0,0,0,.2);text-align:center;font-size:9px;color:var(--ink);display:flex;flex-direction:column;justify-content:center;line-height:11px}
.bubble b{color:var(--teal-dark)}
.hero-title{left:416px;top:70px;text-align:left}
.hero-title .n{font-size:15px;font-weight:700;color:var(--ink);line-height:17px}
.hero-title .n em{font-style:normal;color:var(--teal)}
.hero-title .t{font-size:6.5px;color:var(--muted)}
.pager{left:353px;top:214px;display:flex;gap:4px}
.pager i{width:9px;height:9px;border-radius:50%;background:#fff;border:1px solid #ccc;display:block}
.intro{left:0;top:309px;width:749px;height:253px;background:var(--soft)}
.intro h2{position:absolute;left:0;width:749px;top:12px;text-align:center;font-size:14.5px;font-weight:600;color:var(--teal)}
.intro p.sub{position:absolute;left:0;width:749px;top:30px;text-align:center;font-size:9.5px;color:var(--ink)}
.intro hr{position:absolute;left:106px;top:54px;width:536px;border:0;border-top:1px dashed var(--line)}
.feature{width:152px;height:152px;top:397px;text-align:center}
.feature .ring{position:absolute;inset:0;border-radius:50%;background:var(--white)}
.feature .icon{position:absolute;left:52px;top:-18px;width:48px;height:48px;border-radius:50%;background:var(--teal)}
.feature h3{position:absolute;top:38px;width:100%;font-size:17px;font-weight:600;color:var(--ink)}
.feature p{position:absolute;top:66px;left:12px;width:128px;font-size:6.6px;line-height:8.3px;color:var(--text)}
.btn{position:absolute;left:47px;top:105px;width:58px;height:17px;background:var(--teal);color:#fff;font-size:7px;font-weight:600;line-height:17px;border-radius:2px}
.section-title{font-size:14px;color:var(--ink)}
.section-title b{font-weight:700}
.rule{height:0;border-top:2px dotted #d4d4d4}
.thumb{top:602px;width:119px;height:88px;border:1px solid #ddd;background:#fff;padding:3px}
.thumb .img{width:100%;height:100%;position:relative}
.thumb .cap{position:absolute;left:0;bottom:0;width:100%;height:14px;background:rgba(60,60,60,.65);color:#fff;font-size:7.5px;font-weight:700;text-align:center;line-height:14px}
.arrow{top:632px;font-size:22px;color:#bbb;font-weight:400}
.lower{left:0;top:704px;width:749px;height:254px;background:var(--soft)}
.why-icon{width:30px;height:30px;border-radius:50%;background:#333;color:#fff;text-align:center;line-height:30px;font-size:13px}
.why-box{left:159px;width:206px;height:50px;background:#fff;border:1px solid #e2e2e2;padding:4px 7px}
.why-box h4{font-size:9px;font-weight:400;color:var(--ink);border-bottom:1px solid #eee;padding-bottom:2px;margin-bottom:3px}
.why-box p{font-size:6px;line-height:7.3px;color:var(--muted)}
.avatar{width:36px;height:36px;border-radius:50%;border:3px solid #fff;box-shadow:0 1px 3px rgba(0,0,0,.25);background:linear-gradient(180deg,#e7d2b8,#b9946f)}
.quote{height:42px;background:#e9e9e9;border:1px solid #cfcfcf;box-shadow:1px 1px 2px rgba(0,0,0,.15);padding:4px 7px;font-size:6px;line-height:11px;font-style:italic;color:#444}
.quote .who{font-style:normal;font-size:7.5px;color:var(--teal);background:#dcdcdc;padding:0 6px;margin-right:4px}
.tweet{left:0;top:984px;width:749px;height:31px;background:var(--teal);color:#fff;text-align:center;font-size:7.6px}
.tweet .t1{position:absolute;top:7px;width:100%}
.tweet .t2{position:absolute;top:19px;width:100%;font-size:6px;color:#dff}
.footer{left:0;top:1015px;width:749px;height:157px;background:var(--footer);color:#ddd;font-size:7px;line-height:8.4px}
.footer h5{position:absolute;top:14px;font-size:9px;font-weight:400;color:#eee}
.fcol{position:absolute;top:35px}
.fcol .hl{color:var(--teal-light)}
.news{display:flex;gap:7px;margin-bottom:10px}
.news .img{width:33px;height:27px;background:linear-gradient(135deg,#d8d8d8,#9a6a6a)}
.fdot{display:inline-block;width:16px;height:16px;border-radius:50%;background:#444;margin-right:4px}
.bottom{left:0;top:1172px;width:749px;height:28px;background:var(--footer-deep);color:#ccc;font-size:6.8px;line-height:28px}
.bottom .hl{color:var(--teal-light)}
.bottom nav{position:absolute;right:107px;top:0}
.bottom nav span{padding:0 6px;border-left:1px solid #555}
.bottom nav span:first-child{border-left:0}
</style>
</head>
<body>

<div class="abs topbar">
  <span style="left:108px">&#9742; 555-010-2040</span>
  <span style="left:174px">&#9993; hello@pellbrook.example</span>
  <span style="left:261px">&#9719; Monday - Friday : 8.00 - 20.00</span>
  <i class="dot-social" style="left:585px"></i>
  <i class="dot-social" style="left:606px"></i>
  <i class="dot-social" style="left:627px"></i>
</div>

<header class="abs header">
  <div class="abs brand">
    <div class="brand-name"><em>Gordon</em> Pellbrook</div>
    <div class="brand-tag">LOREM IPSUM IS SIMPLY DUMMY TEXT</div>
  </div>
  <nav class="abs nav">
    <a class="active">Home</a><a>About Us</a><a>Consultations</a><a>Services</a><a>FAQ</a><a>Contact Us</a>
  </nav>
</header>

<section class="abs hero">
  <div class="abs hero-leaf" role="img" aria-label="Soft green foliage in the background"></div>
  <div class="abs portrait" role="img" aria-label="Portrait of Gordon Pellbrook in a light blue blazer"></div>
  <div class="abs bubble" style="left:310px;top:12px">Specializing In<b>Innovation</b></div>
  <div class="abs bubble" style="left:553px;top:12px">Specializing In<b>Technology</b></div>
  <div class="abs bubble" style="left:442px;top:123px">Specializing In<b>Strategy</b></div>
  <div class="abs hero-title">
    <div class="n"><em>Gordon</em> Pellbrook</div>
    <div class="t">LOREM IPSUM IS SIMPLY DUMMY TEXT</div>
  </div>
  <div class="abs pager"><i></i><i></i><i></i><i></i><i></i></div>
</section>

<section class="abs intro">
  <h2>Lorem Ipsum is simply dummy text of the typesetting</h2>
  <p class="sub">industry. Lorem Ipsum has been the industry's</p>
  <hr>
</section>

<div class="abs feature" style="left:107px">
  <div class="ring"></div><div class="icon"></div>
  <h3>Innovation</h3>
  <p>Lorem ipsum dolor sit amet, co ctetuer adipiscing elit, sed di nonummy nibh euismod te.</p>
  <div class="btn">Read More</div>
</div>
<div class="abs feature" style="left:297px">
  <div class="ring"></div><div class="icon"></div>
  <h3>Technology</h3>
  <p>Lorem ipsum dolor sit amet, co ctetuer adipiscing elit, sed di nonummy nibh euismod te.</p>
  <div class="btn">Read More</div>
</div>
<div class="abs feature" style="left:488px">
  <div class="ring"></div><div class="icon"></div>
  <h3>Strategy</h3>
  <p>Lorem ipsum dolor sit amet, co ctetuer adipiscing elit, sed di nonummy nibh euismod te.</p>
  <div class="btn">Read More</div>
</div>

<div class="abs section-title" style="left:106px;top:572px"><b>Recent</b> Works</div>
<div class="abs rule" style="left:204px;top:583px;width:438px"></div>
<div class="abs arrow" style="left:106px">&#10216;</div>
<div class="abs arrow" style="left:633px">&#10217;</div>
<div class="abs thumb" style="left:122px"><div class="img" role="img" aria-label="Team applauding in a meeting" style="background:linear-gradient(135deg,#e6e3dd,#7a6a60)"><div class="cap">LOREM IPSUM</div></div></div>
<div class="abs thumb" style="left:251px"><div class="img" role="img" aria-label="Colleagues working together at a desk" style="background:linear-gradient(135deg,#d9d6d2,#8c4b4b)"><div class="cap">LOREM IPSUM</div></div></div>
<div class="abs thumb" style="left:380px"><div class="img" role="img" aria-label="Business people reviewing papers" style="background:linear-gradient(135deg,#cfd2d4,#4f5559)"><div class="cap">LOREM IPSUM</div></div></div>
<div class="abs thumb" style="left:509px"><div class="img" role="img" aria-label="Presenter at a flip chart" style="background:linear-gradient(135deg,#e2e4e6,#5c6066)"><div class="cap">LOREM IPSUM</div></div></div>

<section class="abs lower"></section>
<div class="abs section-title" style="left:107px;top:716px"><b>Why</b> Choose <b>Us</b></div>
<div class="abs rule" style="left:218px;top:728px;width:146px"></div>
<div class="abs" style="left:122px;top:766px;width:1px;height:176px;background:#ddd"></div>
<div class="abs why-icon" style="left:107px;top:751px">&#9633;</div>
<div class="abs why-icon" style="left:107px;top:822px">+</div>
<div class="abs why-icon" style="left:107px;top:891px">&#10148;</div>
<div class="abs why-box" style="top:751px"><h4>About our company</h4><p>Lorem ipsum dolor sit amet, consectetur adipisicing elit, sed do eiusmod tempor incididunt ut labore et dolore magna aliqua. Ut enim ad minim veniam, quis nostrud</p></div>
<div class="abs why-box" style="top:822px"><h4>Our mission</h4><p>Lorem ipsum dolor sit amet, consectetur adipisicing elit, sed do eiusmod tempor incididunt ut labore et dolore magna aliqua. Ut enim ad minim veniam, quis nostrud</p></div>
<div class="abs why-box" style="top:893px"><h4>What we see in future</h4><p>Lorem ipsum dolor sit amet, consectetur adipisicing elit, sed do eiusmod tempor incididunt ut labore et dolore magna aliqua. Ut enim ad minim veniam, quis nostrud</p></div>

<div class="abs section-title" style="left:385px;top:716px"><b>Clients</b> Testimonial</div>
<div class="abs rule" style="left:516px;top:728px;width:126px"></div>
<div class="abs avatar" style="left:387px;top:764px" role="img" aria-label="Client portrait"></div>
<div class="abs quote" style="left:434px;top:755px;width:208px"><span class="who">Ana Doe, CEO</span>Lorem Ipsum is simply dummy text of the printing and typesetting industry. Lorem Ipsum has been the industry's standard dummy text ever since the 1500s</div>
<div class="abs quote" style="left:386px;top:819px;width:210px">Lorem Ipsum is simply dummy text of the <span class="who" style="float:right">Ana Doe, CEO</span>industry. Lorem Ipsum has been the industry's standard dummy text ever since the 1500s</div>
<div class="abs avatar" style="left:605px;top:828px" role="img" aria-label="Client portrait"></div>
<div class="abs avatar" style="left:387px;top:896px" role="img" aria-label="Client portrait"></div>
<div class="abs quote" style="left:434px;top:884px;width:208px"><span class="who">Ana Doe, CEO</span>Lorem Ipsum is simply dummy text of the printing and typesetting industry. Lorem Ipsum has been the industry's standard dummy text ever since the 1500s</div>

<div class="abs" style="left:366px;top:969px;width:16px;height:16px;border-radius:50%;background:var(--teal)"></div>
<section class="abs tweet">
  <span class="abs" style="left:8px;top:6px;font-size:12px">&#8249;</span>
  <span class="abs" style="right:10px;top:6px;font-size:12px">&#8250;</span>
  <div class="t1">Lorem Ipsum is simply dummy text of the printing and typesetting industry. Lorem Ipsum has been the industry's standard dummy text ever since</div>
  <div class="t2">2 days ago</div>
</section>

<footer class="abs footer">
  <h5 style="left:108px">ABOUT US</h5>
  <div class="fcol" style="left:108px;width:140px">Lorem Ipsum is simply dummy text of the printing and typesetting industry. Lorem Ipsum has been the industry's standard dummy text ever since the 1500s, when an unknown printer took a galley of type and scrambled it to make a type specimen book. It has survived not
    <div style="margin-top:12px"><i class="fdot"></i><i class="fdot"></i><i class="fdot"></i></div>
  </div>
  <h5 style="left:277px">LATEST NEWS</h5>
  <div class="fcol" style="left:277px">
    <div class="news"><div class="img" role="img" aria-label="News thumbnail"></div><div><span class="hl">Lorem Ipsum is</span><br>May 13, 2013</div></div>
    <div class="news"><div class="img" role="img" aria-label="News thumbnail"></div><div><span class="hl">Lorem Ipsum is</span><br>May 13, 2013</div></div>
    <div class="news"><div class="img" role="img" aria-label="News thumbnail"></div><div><span class="hl">Lorem Ipsum is</span><br>May 13, 2013</div></div>
  </div>
  <h5 style="left:410px">CONTACTS</h5>
  <div class="fcol" style="left:410px">Company Address<br><br>Phone: +61 2 5550 1234<br>Mobile: +61 4 5550 4321<br><br><span class="hl">office@pellbrook.example</span></div>
  <h5 style="left:530px">OPENING HOURS</h5>
  <div class="fcol" style="left:530px;width:115px">We can provide free support every day for 24 hours.<br><br>Our office is open:<br>Monday - <span class="hl">Friday: 8am - 5pm</span><br>Saturday: <span class="hl">8am - 1pm</span><br>Sunday: <span class="hl">Closed</span></div>
</footer>

<div class="abs bottom">
  <span class="abs" style="left:108px">&copy; 2013 <span class="hl">Gordon Pellbrook</span>. All Right Reserved</span>
  <nav><span>Home</span><span>About us</span><span>Terms</span><span>Contact</span></nav>
</div>

</body>
</html>
```